Business Card for Sugared Soiree

I have a logo for my candy buffet business, and need a business card designed using that logo. Sugared Soiree designs and builds beautiful and delicious candy and dessert tables for all kinds of events. The card should be simple, modern, graphic, colorful, and use the Sugared Soiree Logo.

Target Market(s)

The target market is people hosting major parties and events. This includes brides getting married, parents hosting birthday parties/Sweet Sixteen/Bar Mitzvah/quinceanera parties, and companies hosting corporate events.

Industry/Entity Type

Business

Requirements
Must have
• The business card must have the logo, with or without the tag line.

The following information must be on the card:

Dana Whitfield
CEO & Candy Stylist
614.392.5071
dana@sugaredsoiree-example.com
Nice to have
• I like the idea of having multiple colors of the same design so that several people receiving cards will each receive a different color. Perhaps 3-5 colors or variations on a basic card design.

```html
<!DOCTYPE html>
<html lang="en">
<head>
<meta charset="utf-8">
<title>Sugared Soiree – Business Card</title>
<link rel="stylesheet" href="https://fonts.googleapis.com/css2?family=Questrial&family=Montserrat:wght@400;700&display=swap">
<style>
  :root {
    --bg: #e9e9ec;
    --card: #ffffff;
    --ink: #111111;
    --green: #12853f;
    --yellow: #f3b02d;
    --blue: #2a8fb0;
    --pink: #e0287a;
    --white: #ffffff;
  }
  html, body {
    margin: 0;
    width: 1200px;
    height: 900px;
    overflow: hidden;
    background: var(--bg);
  }
  .canvas {
    width: 1200px;
    height: 900px;
    display: flex;
    flex-direction: column;
    align-items: center;
    justify-content: center;
    gap: 24px;
  }
  .card {
    position: relative;
    width: 700px;
    height: 400px;
    background: var(--card);
    box-shadow: 0 6px 18px rgba(0,0,0,.18);
    overflow: hidden;
  }
  .stripes {
    position: absolute;
    left: 0;
    right: 0;
    display: flex;
    flex-direction: column;
  }
  .stripes span { display: block; }
  .stripes .s-green { height: 12px; background: var(--green); }
  .stripes .s-yellow { height: 7px; background: var(--yellow); }
  .stripes .s-blue { height: 7px; background: var(--blue); }
  .stripes .s-pink { height: 12px; background: var(--pink); }
  .stripes--top { top: 0; }
  .stripes--bottom { bottom: 0; }

  .brand-name {
    position: absolute;
    margin: 0;
    font-family: "Questrial", sans-serif;
    font-weight: 400;
    color: var(--ink);
    line-height: 1;
    letter-spacing: -0.5px;
    white-space: nowrap;
  }
  .card--front .brand-name {
    left: 0;
    right: 0;
    top: 168px;
    text-align: center;
    font-size: 64px;
  }

  .card--back svg { position: absolute; inset: 0; }
  .card--back .brand-name {
    left: 120px;
    top: 92px;
    font-size: 44px;
  }

  .band-name {
    font-family: "Montserrat", sans-serif;
    font-size: 17px;
    fill: var(--white);
    letter-spacing: 1px;
  }
  .band-name .name { font-weight: 700; }
  .band-contact {
    font-family: "Montserrat", sans-serif;
    font-size: 15px;
    fill: var(--white);
  }
</style>
</head>
<body>
<main class="canvas">

  <section class="card card--front" aria-label="Business card front">
    <div class="stripes stripes--top">
      <span class="s-green"></span><span class="s-yellow"></span><span class="s-blue"></span><span class="s-pink"></span>
    </div>
    <h1 class="brand-name">sugared soiree</h1>
    <div class="stripes stripes--bottom">
      <span class="s-green"></span><span class="s-yellow"></span><span class="s-blue"></span><span class="s-pink"></span>
    </div>
  </section>

  <section class="card card--back" aria-label="Business card back">
    <svg width="700" height="400" viewBox="0 0 700 400">
      <rect x="0" y="0" width="700" height="12" fill="var(--green)"/>
      <rect x="0" y="12" width="700" height="7" fill="var(--yellow)"/>
      <rect x="0" y="19" width="700" height="12" fill="var(--pink)"/>

      <polygon class="band band--pink" points="0,300 700,160 700,210 0,350" fill="var(--pink)"/>
      <polygon class="band band--blue" points="0,350 700,210 700,255 0,395" fill="var(--blue)"/>
      <polygon class="band band--green" points="0,395 700,255 700,400 0,400" fill="var(--green)"/>

      <text class="band-name" transform="translate(250 281) rotate(-11.31)"><tspan class="name">DANA WHITFIELD</tspan> · CEO &amp; CANDY STYLIST</text>

      <g class="contact contact--phone" transform="translate(120 349) rotate(-11.31)">
        <path d="M-8 -7 q3 -3 5 0 l2 3 q1 2 -1 3 q2 4 5 5 q1 -2 3 -1 l3 2 q3 2 0 5 q-4 3 -10 -3 q-7 -7 -7 -14 z" fill="var(--white)" transform="translate(0 -2) scale(0.8)"/>
        <text class="band-contact" x="14" y="5">614.392.5071</text>
      </g>
      <g class="contact contact--email" transform="translate(300 315) rotate(-11.31)">
        <rect x="-10" y="-8" width="20" height="14" fill="none" stroke="var(--white)" stroke-width="1.5"/>
        <polyline points="-10,-8 0,0 10,-8" fill="none" stroke="var(--white)" stroke-width="1.5"/>
        <text class="band-contact" x="18" y="5">dana@sugaredsoiree-example.com</text>
      </g>
    </svg>
    <p class="brand-name">sugared soiree</p>
  </section>

</main>
</body>
</html>
```